Progressive European Honey Business needs minimalistic packaging design

Hello - thank you for your interest in our brief. We are Fizzy Vixens, a London based Honey business, importing only the best honey Europe has to offer. Our values are deeply rooted with in progressive liberal values and we are looking for minimalist packaging, which reflects that.

We are looking for a design, which dimensions fit with our packaging option (Velmor Glass Jar | HEIGHT 90mm | DIAMETER 63mm). We will require a various output files (High Resolution JPEG (CMYK Colors 300 dpi) Source File Ai, PSD, PDF, Printing files (die cut, die folding) and a 3D Mockup of the packaging for use within digital commerce platforms.

We must be able to adjust the free text on the label front and it should include the following:
Brand Name
Honey type
Limited edition No. X / 100 ( X being the number of purchase i.e. 25 / 100)
EU Honey, Single Orgin (Germany)
(c) The net weight (250g)

The back must include room for additional information (again adjustable by us) and the following:
“Unsuitable for children under 12 months”
(b) The appropriate durability declaration

In total, we are looking for
a) A front label
b) A back label
c) A seal (round) including the attached bee and logo included in the Zip file.
Do note that a) & b) can also be combined into one design as long as the symmetry on the jar stays intact.

The final design should communicate modern aesthetics, high quality, that are slightly provocative and pop off the shelves.

Hi folks, sorry for the delay in completing this project, but my business partner had a leak in his house. We planned to finalise our review today, but this will have to wait until it's no longer raining in his livingroom. Our sincere apologies!

• See branding guidelines

• Must follow the branding guideline and fonts provided as attachment

```html
<!DOCTYPE html>
<html lang="en">
<head>
<meta charset="utf-8">
<title>Fizzy Vixens – Front Label</title>
<link rel="stylesheet" href="https://fonts.googleapis.com/css2?family=Alfa+Slab+One&family=Josefin+Sans:wght@400;700&display=swap">
<style>
  :root {
    --label-white: #ffffff;
    --brand-orange: #e8531c;
    --honey-purple: #6e1f6f;
    --band-purple: #7a2b82;
    --ink: #1a1a1a;
    --bee-yellow: #f2c230;
    --bee-black: #1d1d1d;
    --page: #f4f4f2;
  }
  * { margin: 0; padding: 0; box-sizing: border-box; }
  html, body { width: 1200px; height: 881px; overflow: hidden; background: var(--page); }
  .label {
    position: relative;
    width: 1200px;
    height: 881px;
    background: var(--label-white);
    font-family: "Josefin Sans", Arial, sans-serif;
  }
  .brand-name {
    position: absolute;
    top: 92px;
    left: 0;
    width: 100%;
    text-align: center;
    color: var(--brand-orange);
    font-weight: 700;
    font-size: 58px;
    letter-spacing: 2px;
    text-transform: uppercase;
  }
  .mascot {
    position: absolute;
    left: 70px;
    top: 230px;
    width: 290px;
    height: 370px;
  }
  .honey-type {
    position: absolute;
    right: 60px;
    top: 225px;
    text-align: right;
    font-family: "Alfa Slab One", Georgia, serif;
    color: var(--honey-purple);
    font-size: 150px;
    line-height: 1.0;
    text-transform: uppercase;
  }
  .honey-type span { display: block; }
  .edition {
    position: absolute;
    right: 60px;
    top: 585px;
    font-weight: 700;
    font-size: 44px;
    color: var(--ink);
    text-transform: uppercase;
  }
  .info-band {
    position: absolute;
    left: 0;
    top: 720px;
    width: 100%;
    height: 84px;
    background: var(--band-purple);
    color: var(--label-white);
    display: flex;
    align-items: center;
    justify-content: center;
    gap: 36px;
    font-size: 30px;
    text-transform: uppercase;
    padding-top: 6px;
  }
  .info-band .weight { font-weight: 700; }
  .info-band .divider { font-weight: 400; }
</style>
</head>
<body>
  <main class="label">
    <h1 class="brand-name">Fizzy Vixens</h1>

    <svg class="mascot" role="img" aria-label="Illustration of the crowned bee mascot" viewBox="0 0 290 370">
      <defs>
        <linearGradient id="mascotFill" x1="0" y1="0" x2="1" y2="1">
          <stop offset="0" stop-color="#f6d04a"/>
          <stop offset="0.6" stop-color="#e9b72a"/>
          <stop offset="1" stop-color="#3a3226"/>
        </linearGradient>
      </defs>
      <rect x="0" y="0" width="290" height="370" rx="40" fill="url(#mascotFill)"/>
    </svg>

    <h2 class="honey-type"><span>Honey</span><span>Type</span></h2>

    <p class="edition">Limited Edition No. X / 100</p>

    <div class="info-band">
      <span class="weight">Net Weight (250G)</span>
      <span class="divider">|</span>
      <span class="origin">EU Honey, Single Orgin Germany</span>
    </div>
  </main>
</body>
</html>
```